Website Design for Bright Path Learning

The business is called Bright Path Learning - a Drug & Alcohol Education program for Sydney school kids. I wish to create a simple online business card which covers who we are, the programs we offer and why they should choose us. I would like the business page to be very colourful and school-friendly, but with the seriousness of alcohol and drug use. I have attached some pictures and logos for the business. The programs are called 'hold firm' for high school, and 'grow wise' for primary school. The logo is black & white. There is also a photo of the manager with some kids.

```html
<!DOCTYPE html>
<html lang="en">
<head>
<meta charset="utf-8">
<title>Bright Path Learning – Drug &amp; Alcohol Education</title>
<link rel="stylesheet" href="https://fonts.googleapis.com/css2?family=Oswald:wght@300;400;500;600&family=Raleway:wght@300;400&family=Arimo:wght@400;700&display=swap">
<style>
  :root {
    --yellow: #fff000;
    --top-orange: #f4821f;
    --nav-blue: #29abe2;
    --nav-blue-dark: #1b7fae;
    --green: #7fae1c;
    --green-ring: #6f9e12;
    --orange: #f55208;
    --footer-text: #f7931e;
    --ink: #222222;
    --label: #3a3a3a;
    --white: #ffffff;
  }
  * { box-sizing: border-box; margin: 0; padding: 0; }
  html, body { width: 1200px; height: 2539px; overflow: hidden; background: var(--white); }
  body { position: relative; font-family: "Arimo", Arial, sans-serif; color: var(--ink); }

  .abs { position: absolute; }

  /* Header */
  .hero-photo {
    left: 0; top: 0; width: 1200px; height: 550px;
    background: linear-gradient(100deg, #5a5a5a 0%, #bdbdbd 35%, #d8d8d8 60%, #a9a9a9 85%, #cfcfcf 100%);
  }
  .top-strip { left: 0; top: 0; width: 1200px; height: 20px; background: var(--yellow); }
  .top-bar { left: 0; top: 20px; width: 1200px; height: 56px; background: var(--top-orange); }
  .tagline {
    top: 20px; height: 56px; line-height: 56px;
    font-family: "Raleway", sans-serif; font-weight: 400; font-size: 22px; color: var(--white);
  }
  .tagline--left { left: 168px; }
  .tagline--right { left: 772px; }
  .header-badge { left: 0; top: 0; }
  .brand-mark {
    left: 470px; top: 30px; width: 260px; text-align: center;
    font-family: "Oswald", sans-serif; font-weight: 600; font-size: 40px; letter-spacing: 1px;
    color: var(--ink); line-height: 60px;
  }
  .slider-arrow { top: 279px; width: 34px; height: 34px; border-radius: 50%; background: #f7b733; opacity: .9; }
  .slider-arrow--prev { left: 21px; }
  .slider-arrow--next { left: 1141px; }

  /* Nav */
  .main-nav { left: 0; top: 528px; }
  .nav-links {
    left: 127px; top: 530px; width: 948px; height: 66px;
    display: flex; align-items: center; list-style: none;
    font-family: "Oswald", sans-serif; font-weight: 300; font-size: 28px; color: var(--white);
  }
  .nav-links li { position: absolute; top: 14px; white-space: nowrap; text-transform: uppercase; }

  /* Programs band */
  .programs {
    left: 0; top: 596px; width: 1200px; height: 462px;
    background: var(--green);
  }
  .programs-pattern { left: 0; top: 550px; width: 1200px; height: 508px;
    background: radial-gradient(ellipse at 50% 50%, #8cbb2a 0%, var(--green) 70%); }
  .program {
    width: 304px; height: 304px; border-radius: 50%; background: var(--white);
    top: 686px; box-shadow: 0 2px 6px rgba(0,0,0,.15);
  }
  .program--grow { left: 231px; }
  .program--hold { left: 671px; }
  .program-ring {
    position: absolute; left: 16px; top: 16px; width: 272px; height: 272px;
    border-radius: 50%; border: 6px solid var(--green-ring);
  }
  .program-name {
    position: absolute; left: 0; top: 80px; width: 304px; text-align: center;
    font-family: "Oswald", sans-serif; font-weight: 500; font-size: 46px; line-height: 56px;
    color: var(--ink); text-transform: lowercase;
  }
  .program-level {
    position: absolute; left: 0; top: 180px; width: 304px; text-align: center;
    font-family: "Oswald", sans-serif; font-weight: 400; font-size: 29px; line-height: 31px;
    color: var(--label); text-transform: uppercase;
  }

  /* Intro */
  .group-photo {
    left: 152px; top: 1108px; width: 931px; height: 492px;
    background: radial-gradient(ellipse at 50% 45%, #d9b79a 0%, #c78f7a 30%, #9cb3d6 60%, rgba(255,255,255,0) 78%);
  }
  .section-title {
    left: 0; width: 1200px; text-align: center;
    font-family: "Raleway", sans-serif; font-weight: 300; font-size: 40px;
  }
  .intro-title { top: 1630px; color: var(--ink); }
  .section-copy {
    left: 71px; width: 1058px; text-align: center;
    font-size: 13.6px; line-height: 18.6px;
  }
  .intro-copy { top: 1716px; color: var(--ink); }

  /* Why choose us */
  .why { left: 0; top: 1904px; width: 1200px; height: 372px; background: var(--orange); }
  .why-notch { left: 0; top: 1904px; }
  .why-title { top: 2004px; color: var(--white); }
  .why-copy { top: 2096px; color: var(--white); }

  /* Footer */
  .site-footer { left: 0; top: 2276px; width: 1200px; height: 263px; background: var(--yellow); }
  .footer-brand {
    left: 37px; top: 2324px;
    font-family: "Oswald", sans-serif; font-weight: 600; font-size: 44px; line-height: 56px;
    color: var(--footer-text);
  }
  .footer-blurb {
    left: 40px; top: 2398px; width: 320px;
    font-size: 13px; line-height: 15.5px; color: var(--footer-text);
  }
  .footer-links {
    left: 393px; top: 2326px; list-style: none;
    font-family: "Raleway", sans-serif; font-weight: 300; font-size: 27px; line-height: 36px;
    color: var(--footer-text);
  }
  .social { top: 2332px; width: 35px; height: 35px; border-radius: 50%; background: var(--footer-text); }
  .contact-name {
    left: 902px; top: 2322px;
    font-family: "Arimo", sans-serif; font-weight: 700; font-size: 21px; color: var(--footer-text);
  }
  .contact-address {
    left: 902px; top: 2352px; width: 290px;
    font-size: 14px; line-height: 19px; color: var(--footer-text);
  }
  .contact-phone {
    left: 902px; top: 2410px; height: 40px;
    display: flex; align-items: center; gap: 8px;
    font-family: "Raleway", sans-serif; font-weight: 400; font-size: 27px; color: var(--footer-text);
  }
  .contact-email { left: 905px; top: 2444px; font-size: 14px; color: var(--footer-text); }
  .footer-rule { left: 0; top: 2483px; width: 1200px; height: 1px; background: rgba(247,147,30,.35); }
  .copyright { left: 37px; top: 2498px; font-size: 12px; color: var(--footer-text); }
  .legal { left: 905px; top: 2498px; font-size: 12px; color: var(--footer-text); }
</style>
</head>
<body>

<header>
  <div class="abs hero-photo" role="img" aria-label="Black and white photo of the program manager in a blazer leaning against a wall, with a family of students standing behind him"></div>
  <div class="abs top-strip"></div>
  <div class="abs top-bar"></div>
  <p class="abs tagline tagline--left">A Drug &amp; Alcohol&nbsp; Education</p>
  <p class="abs tagline tagline--right">Program for Sydney School Kids</p>
  <svg class="abs header-badge" width="1200" height="120" viewBox="0 0 1200 120" aria-hidden="true">
    <polygon points="443,76 478,76 478,112" fill="#bdbdbd"/>
    <polygon points="757,76 722,76 722,112" fill="#bdbdbd"/>
    <polygon points="443,76 460,14 740,14 757,76 722,76 722,96 478,96 478,76" fill="#ffffff"/>
  </svg>
  <div class="abs brand-mark">BRIGHT PATH</div>
  <div class="abs slider-arrow slider-arrow--prev" aria-label="Previous slide"></div>
  <div class="abs slider-arrow slider-arrow--next" aria-label="Next slide"></div>
</header>

<div class="abs programs-pattern" role="img" aria-label="Green background with chalk-style doodles of drugs, bottles, pills and molecules"></div>

<nav>
  <svg class="abs main-nav" width="1200" height="80" viewBox="0 0 1200 80" aria-hidden="true">
    <polygon points="112,2 127,2 127,40" fill="var(--nav-blue-dark)"/>
    <polygon points="1088,2 1073,2 1073,40" fill="var(--nav-blue-dark)"/>
    <polygon points="112,2 1088,2 1075,68 127,68" fill="var(--nav-blue)"/>
  </svg>
  <ul class="abs nav-links">
    <li style="left:101px">Home</li>
    <li style="left:225px">Who we are</li>
    <li style="left:427px">The programs</li>
    <li style="left:643px">Why choose us</li>
  </ul>
</nav>

<section aria-label="Programs">
  <div class="abs program program--grow">
    <div class="program-ring"></div>
    <p class="program-name">grow wise</p>
    <p class="program-level">Program for<br>High School</p>
  </div>
  <div class="abs program program--hold">
    <div class="program-ring"></div>
    <p class="program-name">hold firm</p>
    <p class="program-level">Program for<br>High School</p>
  </div>
</section>

<section aria-label="Who we are">
  <div class="abs group-photo" role="img" aria-label="Photo of a large group of smiling school students, older kids standing and younger kids kneeling in front"></div>
  <h1 class="abs section-title intro-title">a Drug &amp; Alcohol Education program for Sydney school kids</h1>
  <p class="abs section-copy intro-copy">Lorem ipsum dolor sit amet, consectetuer adipiscing elit, sed diam nonummy nibh euismod tincidunt ut laoreet dolore magna aliquam erat volutpat. Ut wisi enim ad minim veniam, quis nostrud exerci tation ullamcorper suscipit lobortis nisl ut aliquip ex ea commodo consequat. Duis autem vel eum iriure dolor in hendrerit in vulputate velit esse molestie consequat, vel illum dolore eu feugiat nulla facilisis at vero eros et accumsan et iusto odio dignissim qui blandit praesent luptatum zzril delenit augue duis dolore te feugait nulla facilisi. Nam liber tempor cum soluta nobis eleifend option congue nihil imperdiet doming id quod mazim placerat facer possim assum.</p>
</section>

<section aria-label="Why choose us">
  <div class="abs why"></div>
  <svg class="abs why-notch" width="1200" height="24" viewBox="0 0 1200 24" aria-hidden="true">
    <polygon points="578,0 624,0 601,22" fill="#ffffff"/>
  </svg>
  <h2 class="abs section-title why-title">Why Choose Us?</h2>
  <p class="abs section-copy why-copy">Lorem ipsum dolor sit amet, consectetuer adipiscing elit, sed diam nonummy nibh euismod tincidunt ut laoreet dolore magna aliquam erat volutpat. Ut wisi enim ad minim veniam, quis nostrud exerci tation ullamcorper suscipit lobortis nisl ut aliquip ex ea commodo consequat. Duis autem vel eum iriure dolor in hendrerit in vulputate velit esse molestie consequat, vel illum dolore eu feugiat nulla facilisis at vero eros et accumsan et iusto odio dignissim qui blandit praesent luptatum zzril delenit augue duis dolore te feugait nulla facilisi. Nam liber tempor cum soluta nobis eleifend option congue nihil imperdiet doming id quod mazim placerat facer possim assum.</p>
</section>

<footer>
  <div class="abs site-footer"></div>
  <div class="abs footer-brand">BRIGHT PATH</div>
  <p class="abs footer-blurb">Lorem ipsum dolor sit amet, consectetuer adipiscing elit, sed diam nonummy nibh euismod tincidunt ut laoreet dolore magna.</p>
  <ul class="abs footer-links">
    <li>Home</li>
    <li>Who we are</li>
    <li>The programs</li>
    <li>Why Choose us</li>
  </ul>
  <div class="abs social" style="left:628px" aria-label="Social link"></div>
  <div class="abs social" style="left:675px" aria-label="Social link"></div>
  <div class="abs social" style="left:721px" aria-label="Social link"></div>
  <div class="abs social" style="left:768px" aria-label="Social link"></div>
  <p class="abs contact-name">Bright Path Learning</p>
  <p class="abs contact-address">88 Harbour Lane Studio 12<br>Glebe, Australia 200037</p>
  <p class="abs contact-phone">
    <svg width="34" height="34" viewBox="0 0 34 34" aria-hidden="true">
      <circle cx="17" cy="17" r="15" fill="none" stroke="var(--footer-text)" stroke-width="2.5"/>
      <path d="M11.5 9.5c1-.8 2-.6 2.6.3l1.5 2.4c.5.8.3 1.6-.4 2.2l-1 .8c.9 2 2.5 3.6 4.5 4.5l.8-1c.6-.7 1.4-.9 2.2-.4l2.4 1.5c.9.6 1.1 1.6.3 2.6l-1 1.2c-.8.9-2 1.2-3.2.8-4.6-1.6-8.2-5.2-9.8-9.8-.4-1.2-.1-2.4.8-3.2z" fill="var(--footer-text)"/>
    </svg>
    010.555.0142
  </p>
  <p class="abs contact-email">hello@brightpathlearning.example</p>
  <div class="abs footer-rule"></div>
  <p class="abs copyright">© Copyright Bright Path Learning 2014. All Rights Reserved</p>
  <p class="abs legal">Terms &nbsp;|&nbsp; Privacy</p>
</footer>

</body>
</html>
```